Real Estate Open House A Frame Sign

The sign is 22" wide and 28" tall. This sign is used to post around the neighbourhood to direct people to an open house (home that is for sale). It is also used for self-promotion.

Designwise
- I just want something with a modern look, simple and clean.
- I want my picture and business logo on the left side.
- On the right side, website (www.lumwick-realestate.com) and my phone (555-374-9126), then a blank space where I can write an address when I need to.

I'm not sure how I want the overall design look. I'm very open-minded and I'm depending on your creative mind to come up with something.

If you have any questions, please let me know.

```html
<!DOCTYPE html>
<html lang="en">
<head>
<meta charset="utf-8">
<title>Open House Sign – Lumwick Real Estate</title>
<link rel="stylesheet" href="https://fonts.googleapis.com/css2?family=Cinzel:wght@600;700&family=Montserrat:wght@300;400;600&display=swap">
<style>
  :root {
    --backdrop: #e9e6e1;
    --brand-blue: #023f7f;
    --slate: #4f5257;
    --paper: #ffffff;
    --photo-dark: #262a33;
    --photo-light: #3b4150;
  }
  * { margin: 0; padding: 0; box-sizing: border-box; }
  html, body {
    width: 1200px; height: 1200px; overflow: hidden;
    background: var(--backdrop);
  }
  .sign {
    position: absolute; left: 167px; top: 50px;
    width: 866px; height: 1100px;
    border-radius: 18px; overflow: hidden;
    background: var(--slate);
    box-shadow: 0 14px 40px rgba(0,0,0,.28);
    color: var(--paper);
  }
  .brand-band {
    position: absolute; left: 0; top: 0; width: 100%; height: 425px;
    background: var(--brand-blue);
  }
  .brand-name {
    position: absolute; left: 117px; top: 175px; width: 410px;
    font-family: "Montserrat", sans-serif; font-weight: 300;
    font-size: 74px; line-height: 1; letter-spacing: 2px;
  }
  .brand-tagline {
    position: absolute; left: 119px; top: 285px;
    font-family: "Montserrat", sans-serif; font-weight: 600;
    font-size: 30px; letter-spacing: 11px; line-height: 1;
  }
  .agent-photo {
    position: absolute; left: 570px; top: 30px; width: 262px; height: 395px;
    background: linear-gradient(180deg, var(--photo-light) 0%, var(--photo-dark) 100%);
    border-radius: 120px 120px 0 0;
  }
  .address-strip {
    position: absolute; left: 0; top: 425px; width: 100%; height: 117px;
    background: var(--paper);
  }
  .details {
    position: absolute; left: 0; top: 542px; width: 100%;
    text-align: center;
  }
  .headline {
    margin-top: 18px;
    font-family: "Cinzel", serif; font-weight: 700;
    font-size: 84px; line-height: 1; letter-spacing: 4px;
  }
  .hosted-by {
    margin-top: 12px;
    font-family: "Montserrat", sans-serif; font-weight: 400;
    font-size: 34px; letter-spacing: 6px; line-height: 1;
  }
  .agent-name {
    margin-top: 28px;
    font-family: "Cinzel", serif; font-weight: 700;
    font-size: 74px; line-height: 1.08; letter-spacing: 26px;
    padding-left: 26px;
  }
  .phone {
    margin-top: 42px;
    font-family: "Cinzel", serif; font-weight: 700;
    font-size: 62px; line-height: 1; letter-spacing: 3px;
  }
  .website {
    margin-top: 6px;
    font-family: "Montserrat", sans-serif; font-weight: 600;
    font-size: 24px; letter-spacing: 2.5px; line-height: 1;
  }
  .license {
    margin-top: 20px;
    font-family: "Montserrat", sans-serif; font-weight: 600;
    font-size: 26px; letter-spacing: 1px; line-height: 1;
  }
</style>
</head>
<body>
  <main class="sign">
    <header class="brand-band">
      <div class="brand-name">LUMWICK</div>
      <div class="brand-tagline">REAL ESTATE</div>
      <div class="agent-photo" role="img" aria-label="Portrait photo of the agent in a dark suit with arms crossed"></div>
    </header>
    <div class="address-strip" aria-label="Blank space for writing the property address"></div>
    <section class="details">
      <h1 class="headline">OPEN HOUSE</h1>
      <p class="hosted-by">HOSTED BY</p>
      <p class="agent-name">DALE<br>MORROW</p>
      <p class="phone">555-374-9126</p>
      <p class="website">WWW.LUMWICK-REALESTATE.COM</p>
      <p class="license">DRE #04827316</p>
    </section>
  </main>
</body>
</html>
```